Bussiness card/stationary for healthcare consulting company
Keltova Healthcare Solutions
Use same font as used in my logo
Franklin Gothic Demi Cond
Professional
Daniel Prescott
CEO
5183 NE Bellcourt Lane
Dallmoor, OK 66609-2871
785-461-xxxx
dprescott@keltova.org
keltova.org
Please have the name, title, address, phone, etc. be fields that can be editted for updates and others needing business cards. I would like to be able to edit everything on the card except the logo and design. I need business cards, stationary and envelopes.

```html
<!DOCTYPE html>
<html lang="en">
<head>
<meta charset="utf-8">
<title>Keltova Healthcare Solutions – Business Card</title>
<link rel="stylesheet" href="https://fonts.googleapis.com/css2?family=Archivo+Narrow:wght@400;600;700&family=Libre+Franklin:wght@400;500&display=swap">
<style>
  :root{
    --teal:#1f7f80;
    --teal-dark:#17686a;
    --grey:#6d6e70;
    --grey-light:#a7a8aa;
    --ink:#3c3d3f;
    --paper:#ffffff;
    --backdrop:#e9eaeb;
  }
  *{box-sizing:border-box;margin:0;padding:0}
  html,body{width:1200px;height:838px;overflow:hidden;background:var(--backdrop)}
  .stage{width:1200px;height:838px;display:flex;flex-direction:column;align-items:center;justify-content:center;gap:34px}
  .card{position:relative;width:660px;height:377px;background:var(--paper);box-shadow:0 6px 18px rgba(0,0,0,.12);overflow:hidden}

  /* front */
  .brand{position:absolute;left:46px;top:140px;display:flex;align-items:center;gap:14px}
  .brand-dot{width:34px;height:34px;border-radius:50%;background:var(--teal)}
  .brand-name{font-family:"Archivo Narrow",sans-serif;font-weight:700;font-size:52px;letter-spacing:1px;color:var(--teal);line-height:1}
  .divider{position:absolute;left:318px;top:84px;width:1px;height:190px;background:var(--grey-light)}
  .contact{position:absolute;left:336px;top:88px;font-family:"Libre Franklin",sans-serif;color:var(--ink)}
  .contact-name{font-family:"Archivo Narrow",sans-serif;font-weight:600;font-size:29px;color:var(--teal);line-height:1.05}
  .contact-title{font-size:12px;color:var(--grey);margin-top:2px}
  .contact-address{font-size:12.5px;line-height:1.4;margin-top:14px;color:var(--grey)}
  .contact-lines{list-style:none;margin-top:14px;font-size:12.5px;line-height:1.55;color:var(--grey)}
  .contact-lines li{display:flex;align-items:center;gap:8px}
  .contact-lines svg{width:12px;height:12px;fill:var(--ink)}
  .bands{position:absolute;left:0;bottom:0;width:660px;height:80px}
  .website{position:absolute;right:34px;bottom:14px;font-family:"Libre Franklin",sans-serif;font-size:13px;letter-spacing:5px;color:#fff}

  /* back */
  .back-brand{position:absolute;inset:0;display:flex;align-items:center;justify-content:center;gap:18px}
  .back-brand .brand-dot{width:54px;height:54px;background:var(--grey)}
  .back-brand .brand-name{font-size:64px}
</style>
</head>
<body>
<main class="stage">
  <section class="card card-front" aria-label="Business card front">
    <div class="brand">
      <span class="brand-dot"></span>
      <span class="brand-name">KELTOVA</span>
    </div>
    <div class="divider"></div>
    <div class="contact">
      <h1 class="contact-name">Daniel Prescott</h1>
      <p class="contact-title">CEO</p>
      <p class="contact-address">5183 NE Bellcourt Lane<br>Dallmoor, OK 66609-2871</p>
      <ul class="contact-lines">
        <li><svg viewBox="0 0 24 24"><path d="M6.6 10.8a15.1 15.1 0 0 0 6.6 6.6l2.2-2.2a1 1 0 0 1 1-.25 11.4 11.4 0 0 0 3.6.57 1 1 0 0 1 1 1V20a1 1 0 0 1-1 1A17 17 0 0 1 3 4a1 1 0 0 1 1-1h3.5a1 1 0 0 1 1 1c0 1.25.2 2.45.57 3.57a1 1 0 0 1-.25 1z"/></svg>555-461-xxxx</li>
        <li><svg viewBox="0 0 24 24"><path d="M6 2h10l2 2v5H6zM4 10h16a2 2 0 0 1 2 2v8H2v-8a2 2 0 0 1 2-2zm3 4v4h10v-4z"/></svg>555-461-xxxx</li>
        <li><svg viewBox="0 0 24 24"><path d="M2 5h20v14H2zm2 2v.5l8 5 8-5V7z"/></svg>dprescott@keltova.org</li>
      </ul>
    </div>
    <svg class="bands" viewBox="0 0 660 80" aria-hidden="true">
      <polygon points="0,50 300,50 318,80 0,80" fill="var(--teal)"/>
      <polygon points="318,80 330,36 660,36 660,80" fill="var(--grey)"/>
      <polygon points="300,50 318,80 330,36 322,36" fill="var(--teal-dark)"/>
    </svg>
    <p class="website">www.keltova.org</p>
  </section>

  <section class="card card-back" aria-label="Business card back">
    <div class="back-brand">
      <span class="brand-dot"></span>
      <span class="brand-name">KELTOVA</span>
    </div>
  </section>
</main>
</body>
</html>
```